Website for a web design agency

We are a website and marketing agency. We do website design, development, and well as Brindle and Quorvia advertising and analytics. We ourselves need a new website for our own brand. We are working on some designs in-house with our own designers, but we also wanted to see what outside designers would come up with.
We are starting off with the homepage, and here is the breakdown of the sections:
https://files.brindlework.example/sheet/d/7kqTr2VnPLwXeHsaMcY4oBfJzuGNtKdWiEh3Rx9pLmQb/view?mode=share
This doc also has many links to sites we have done, which you can take screenshots of for the portfolio section.
In terms of the "look" I am going for, I want to look high-end and very beautiful designs. I found this website that I like a lot that you can use some of the elements of, just as a starting point:
http://velmarkstudio.example/layouts/pixelbarn/html/ostrevo/index.html and here is another design option they have http://velmarkstudio.example/layouts/pixelbarn/html/ostrevo/index-4.html
I'm also uploading my logo. The logo matches the gold and black look from these websites, but I would be open to switching to another color scheme if needed.
This is the link to my very old website, which you can use for some of the dummy text, and a pic of myself. I will be taking more pics of myself:
https://theplumtreeandwillowgroup.example/
We need a homepage and a portfolio page right now, but if you are the winner, we will be hiring you to make additional pages.
Updates
More designs continue to come in even today, and I want to make sure no other designers are still submitting designs.
Target Market(s)
medium and large businesses owners, and non-profits
Number of Pages Required
1 page

```html
<!DOCTYPE html>
<html lang="en">
<head>
<meta charset="utf-8">
<title>Halvard Strategies — We Build Value</title>
<link href="https://fonts.googleapis.com/css2?family=Roboto:wght@400;500;700;900&display=swap" rel="stylesheet">
<style>
:root{
  --bg:#1f1f1f;
  --bg-strip:#242424;
  --gold:#f0b429;
  --gold-dark:#e3a81f;
  --white:#ffffff;
  --muted:#cfcfcf;
  --faint:#3d3d3d;
  --coral:#f26a5b;
  --orange:#f7a55a;
  --violet:#7b7fdb;
  --tile-blue:#0a4fc4;
  --tile-purple:#4a3aa0;
  --tile-rose:#ef4d6a;
  --tile-salmon:#f6a596;
  --tile-coral:#fd5e4e;
  --tile-sky:#1578d6;
  --ink:#555555;
}
*{margin:0;padding:0;box-sizing:border-box}
html,body{width:1200px;height:3632px;overflow:hidden}
body{background:var(--bg);font-family:'Roboto',sans-serif;color:var(--white);position:relative}
.abs{position:absolute}

/* nav */
.site-header{position:absolute;left:0;top:0;width:1200px;height:89px;background:var(--bg)}
.brand{position:absolute;left:75px;top:27px;color:var(--gold);font-weight:700;font-size:20px;letter-spacing:1px;text-transform:uppercase;display:flex;align-items:center;gap:10px}
.brand-mark{width:14px;height:14px;background:var(--gold)}
.main-nav a{position:absolute;top:35px;font-size:13px;color:var(--white);text-decoration:none}
.nav-cta{position:absolute;left:1008px;top:24px;width:116px;height:38px;background:var(--gold);color:var(--white);font-size:13px;display:flex;align-items:center;justify-content:center}

/* hero */
.hero{position:absolute;left:0;top:89px;width:1200px;height:505px;background:var(--bg)}
.hero-photo{position:absolute;left:532px;top:0;width:668px;height:505px;background:linear-gradient(135deg,#6b6357 0%,#3f4a52 45%,#1d2a36 100%)}
.hero-title{position:absolute;left:73px;top:92px;font-size:79px;font-weight:700;line-height:1;letter-spacing:-0.5px}
.hero-title .mark{position:relative;display:inline-block}
.hero-title .mark::after{content:"";position:absolute;left:4px;right:0;bottom:-2px;height:8px;background:var(--gold);z-index:-1}
.hero-sub{position:absolute;left:73px;top:214px;width:400px;font-size:18px;line-height:34px;color:#e8e8e8}
.btn{position:absolute;top:328px;height:51px;display:flex;align-items:center;justify-content:center;font-size:18px;font-weight:500}
.btn-solid{left:73px;width:198px;background:var(--gold);color:var(--white)}
.btn-outline{left:298px;width:145px;border:2px solid var(--gold);color:var(--gold)}

/* client strip */
.clients{position:absolute;left:0;top:594px;width:1200px;height:97px;background:var(--bg-strip)}
.clients span{position:absolute;top:32px;font-size:26px;font-weight:700;color:var(--faint)}

/* section headings */
.section-title{position:absolute;left:0;width:1200px;text-align:center;font-size:51px;font-weight:700}
.section-sub{position:absolute;left:0;width:1200px;text-align:center;font-size:15px;color:var(--faint)}

/* services */
.service{position:absolute;width:260px}
.service-icon{width:70px;height:70px;display:flex;align-items:center;justify-content:center}
.service-icon svg{width:36px;height:36px;fill:none;stroke:#fff;stroke-width:2;stroke-linecap:round;stroke-linejoin:round}
.service h3{margin-top:25px;font-size:16px;font-weight:500}
.service p{margin-top:18px;font-size:13px;line-height:26px;color:var(--muted)}

/* portfolio */
.work{position:absolute;width:522px;height:340px;overflow:hidden}
.work h4{position:absolute;left:30px;top:20px;font-size:17px;font-weight:500}
.work .work-type{position:absolute;left:30px;top:46px;font-size:14px}
.work .shot{position:absolute}

/* testimonials */
.testimonials{position:absolute;left:0;top:2788px;width:1200px;height:844px;background:var(--gold)}
.t-title{position:absolute;left:0;top:40px;width:1200px;text-align:center;font-size:51px;font-weight:700;color:var(--white)}
.t-sub{position:absolute;left:0;top:112px;width:1200px;text-align:center;font-size:16px;color:#f7d27d}
.stars{position:absolute;left:500px;top:172px}
.t-tag{position:absolute;left:0;top:236px;width:1200px;text-align:center;font-size:16px;font-weight:500;color:var(--white)}
.quote-card{position:absolute;left:244px;top:282px;width:712px;height:361px;background:var(--white);padding:38px 38px;text-align:center;color:var(--ink);font-size:14.5px;line-height:30px}
.quote-card p+p{margin-top:26px}
.quote-card::after{content:"";position:absolute;left:148px;bottom:-26px;border-left:26px solid transparent;border-right:26px solid transparent;border-top:26px solid var(--white)}
.arrow{position:absolute;top:427px}
.avatar{position:absolute;left:348px;top:692px;width:107px;height:107px;border-radius:50%;background:linear-gradient(160deg,#b6895c,#6d4a34);border:3px solid #f5c85a}
.person-name{position:absolute;left:475px;top:724px;font-size:22px;font-weight:500;color:var(--white)}
.person-role{position:absolute;left:475px;top:754px;font-size:18px;color:var(--white)}
</style>
</head>
<body>

<header class="site-header">
  <div class="brand"><span class="brand-mark"></span>Halvard Strategies</div>
  <nav class="main-nav">
    <a style="left:491px">Home</a>
    <a style="left:574px">Services</a>
    <a style="left:675px">Portfolio</a>
    <a style="left:777px">Testimonials</a>
    <a style="left:901px">Our Team</a>
  </nav>
  <a class="nav-cta">Contact Us</a>
</header>

<section class="hero">
  <div class="hero-photo" role="img" aria-label="Office workspace with desks, monitors, plants and shelves"></div>
  <h1 class="hero-title">We Build <span class="mark">Value</span></h1>
  <p class="hero-sub">Enterprise Level Website Development and Online Marketing</p>
  <a class="btn btn-solid">See how we do it</a>
  <a class="btn btn-outline">Contact Us</a>
</section>

<section class="clients">
  <span style="left:75px">Ostrane</span>
  <span style="left:308px">Veldmark</span>
  <span style="left:560px">Pellow</span>
  <span style="left:786px">Brask</span>
  <span style="left:983px">Lumero</span>
</section>

<h2 class="section-title" style="top:772px">What we do</h2>
<p class="section-sub" style="top:839px">These are the things we crush</p>

<div class="service" style="left:76px;top:949px">
  <div class="service-icon" style="background:var(--coral)"><svg viewBox="0 0 24 24"><circle cx="12" cy="12" r="9"/><path d="M3 12h18M12 3c3 3 3 15 0 18M12 3c-3 3-3 15 0 18"/></svg></div>
  <h3>Websites</h3>
  <p>Lorem ipsum dolor sit amet, consecte-tur adipisicing elit, sed do eiusmod</p>
</div>
<div class="service" style="left:488px;top:949px">
  <div class="service-icon" style="background:var(--orange)"><svg viewBox="0 0 24 24"><rect x="4" y="4" width="16" height="16" rx="2"/><path d="M4 9h16M8 13h8M8 16h5"/></svg></div>
  <h3>Landing Pages</h3>
  <p>Lorem ipsum dolor sit amet, consecte-tur adipisicing elit, sed do eiusmod</p>
</div>
<div class="service" style="left:894px;top:949px">
  <div class="service-icon" style="background:var(--violet)"><svg viewBox="0 0 24 24"><circle cx="12" cy="12" r="9"/><path d="M15 9c-1-1.5-6-1.5-6 1s6 1.5 6 4-5 2.5-6 1M12 6v12"/></svg></div>
  <h3>Donation Pages</h3>
  <p>Lorem ipsum dolor sit amet, consecte-tur adipisicing elit, sed do eiusmod</p>
</div>
<div class="service" style="left:76px;top:1205px">
  <div class="service-icon" style="background:var(--coral)"><svg viewBox="0 0 24 24"><path d="M4 20h16M6 20v-5M10 20v-7M14 20v-6M18 20v-9M5 13l5-4 3 2 6-6M16 5h3v3"/></svg></div>
  <h3>PPC and Funnels</h3>
  <p>Lorem ipsum dolor sit amet, consecte-tur adipisicing elit, sed do eiusmod</p>
</div>
<div class="service" style="left:488px;top:1205px">
  <div class="service-icon" style="background:var(--orange)"><svg viewBox="0 0 24 24"><circle cx="12" cy="12" r="9"/><path d="M10 8l6 4-6 4z"/></svg></div>
  <h3>VIdeo Marketing</h3>
  <p>Lorem ipsum dolor sit amet, consecte-tur adipisicing elit, sed do eiusmod</p>
</div>
<div class="service" style="left:894px;top:1205px">
  <div class="service-icon" style="background:var(--violet)"><svg viewBox="0 0 24 24"><circle cx="10" cy="10" r="6"/><path d="M15 15l5 5"/></svg></div>
  <h3>Analysis &amp; Optimization</h3>
  <p>Lorem ipsum dolor sit amet, consecte-tur adipisicing elit, sed do eiusmod</p>
</div>

<h2 class="section-title" style="top:1505px">Portfolio</h2>
<p class="section-sub" style="top:1572px">Lorem ipsum is simply a dummy text used</p>

<article class="work" style="left:75px;top:1646px;background:var(--tile-blue)">
  <h4>Orsan Productions</h4><p class="work-type">Production Company</p>
  <div class="shot" role="img" aria-label="Production company homepage screenshot" style="left:77px;top:100px;width:370px;height:240px;background:linear-gradient(180deg,#f4f4f4 0 8%,#123a7a 8% 68%,#ffffff 68%)"></div>
</article>
<article class="work" style="left:602px;top:1646px;background:var(--tile-purple)">
  <h4>H Castell Group</h4><p class="work-type">Construction Management</p>
  <div class="shot" role="img" aria-label="Construction firm website shown on two desktop monitors" style="left:70px;top:92px;width:390px;height:226px;background:linear-gradient(135deg,#e6e6ea 0 45%,#5a4e7a 45% 100%);border-radius:6px"></div>
</article>
<article class="work" style="left:75px;top:1990px;background:var(--tile-rose)">
  <h4>Noa Pertel</h4><p class="work-type">Lifestyle Coach with 15 yrs Experience</p>
  <div class="shot" role="img" aria-label="Coaching website with sunset and sprouting plant header" style="left:88px;top:92px;width:362px;height:234px;background:linear-gradient(180deg,#f6f6f6 0 16%,#e96a4a 16%,#7a2d3a 100%)"></div>
</article>
<article class="work" style="left:602px;top:1990px;background:linear-gradient(180deg,var(--tile-salmon),#f58d70)">
  <h4>Ostrane</h4><p class="work-type">Only Palette you'll ever need</p>
  <div class="shot" role="img" aria-label="Makeup palette product website" style="left:70px;top:100px;width:382px;height:222px;background:linear-gradient(135deg,#fde4df,#f6c3bb)"></div>
</article>
<article class="work" style="left:75px;top:2334px;background:var(--tile-coral)">
  <h4>Lirandel</h4><p class="work-type">Psychotherapist &amp; Healer</p>
  <div class="shot" role="img" aria-label="Therapist website shown on two desktop monitors" style="left:60px;top:92px;width:400px;height:222px;background:linear-gradient(135deg,#ffffff 0 55%,#efe6dd 55%);border-radius:6px"></div>
</article>
<article class="work" style="left:602px;top:2334px;background:var(--tile-sky)">
  <h4>Quillcoin</h4><p class="work-type">Cryptocurrency Exchange</p>
  <div class="shot" role="img" aria-label="Cryptocurrency exchange homepage screenshot" style="left:78px;top:108px;width:370px;height:232px;background:linear-gradient(180deg,#2b2a8a,#163e92)"></div>
</article>

<section class="testimonials">
  <h2 class="t-title">Track Recod People Want to Talk About</h2>
  <p class="t-sub">Your trusted team of experts</p>
  <svg class="stars" width="200" height="40" viewBox="0 0 200 40" fill="#f7c64a" stroke="#fbe08e" stroke-width="1">
    <polygon points="16,12 19,20 28,20 21,25 24,34 16,29 8,34 11,25 4,20 13,20"/>
    <polygon points="58,6 61,14 70,14 63,19 66,28 58,23 50,28 53,19 46,14 55,14"/>
    <polygon points="100,2 103,10 112,10 105,15 108,24 100,19 92,24 95,15 88,10 97,10"/>
    <polygon points="142,6 145,14 154,14 147,19 150,28 142,23 134,28 137,19 130,14 139,14"/>
    <polygon points="184,12 187,20 196,20 189,25 192,34 184,29 176,34 179,25 172,20 181,20"/>
  </svg>
  <p class="t-tag">You have the ideas. We have the tools to bring them to life.</p>
  <svg class="arrow" style="left:75px" width="38" height="72" viewBox="0 0 38 72"><path d="M36 2L2 36l34 34" fill="none" stroke="#fff" stroke-width="3"/></svg>
  <svg class="arrow" style="left:1086px" width="38" height="72" viewBox="0 0 38 72"><path d="M2 2l34 34L2 70" fill="none" stroke="#fff" stroke-width="3"/></svg>
  <blockquote class="quote-card">
    <p>Lorem ipsum dolor sit amet, consectetur adipisicing elit, sed do eiusmod tempor incididunt ut labore et dolore magna aliqua. Ut enim ad minim veniam, quis nostrud exercitation ullamco laboris nisi ut aliquip ex ea commodo consequat. Duis aute irure dolor in reprehenderit in velit esse cillum dolore eu fugiat nulla pariatur. Excepteur sint occaecat cupidatat non proident, sunt in culpa qui officia deserunt mollit anim id est laborum. Sed ut perspiciatis unde omnis</p>
    <p>Lorem ipsum dolor sit amet, consectetur adipisicing elit, sed do eiusmod tempor incididunt ut labore et dolore magna aliqua. Ut enim ad minim veniam, quis nostrud exercitation ullamco laboris nisi ut aliquip ex ea commodo consequat. Duis aute irure dolor in reprehenderit in</p>
  </blockquote>
  <div class="avatar" role="img" aria-label="Portrait photo of the client"></div>
  <p class="person-name">Marta Fennick</p>
  <p class="person-role">Chief clinical operations officer</p>
</section>

</body>
</html>
```